TR Advisory Business Cards - High End AV / Low Voltage Company

We are low voltage AV company that specializes in high end clients on the residential side and larger businesses on the commercial side. We want something modern, tech looking but also something that is extremely professional looking. We have uploaded our logos and postcards we already have in the field. Along with a picture of one of our wrapped vans. Our website is at www.trvadvisory.example and our primary colors are the orange, green, grey and blue all military color finishes.

We are interesting in the slogans "Pairing You with the Right Technology" or "Leading the Lowcountry in Tech"

Target Market(s)

We focus on 70% Commercial and 30% Residential Customers

Industry/Entity Type

Low Voltage, AV Company

Contact Information for Business Card

Name - Dorian Fairweather, Title - Owner, Office Phone - 555-714-3096, Mobile Phone - 555-802-4173, E-Mail - d@trvadvisory.example, Website: www.trvadvisory.example

Font styles to use
Sans Serif

Requirements
Must have
• Must have Name, Title, Work Phone & Mobile, Website and Logo.
Nice to have
• We want something that will impress our higher end clients with a great logo
Should not have
• Too traditional or plain.

```html
<!DOCTYPE html>
<html lang="en">
<head>
<meta charset="utf-8">
<title>TR Advisory — Business Card</title>
<link rel="stylesheet" href="https://fonts.googleapis.com/css2?family=Montserrat:wght@500;600&display=swap">
<style>
  :root {
    --backdrop: #808080;
    --card-white: #ffffff;
    --brand-orange: #e8522f;
    --brand-orange-light: #ee6a3c;
    --logo-orange: #ea6a3a;
    --text-light: #ffffff;
  }
  * { margin: 0; padding: 0; box-sizing: border-box; }
  html, body {
    width: 1200px;
    height: 1000px;
    overflow: hidden;
    background: var(--backdrop);
    font-family: "Montserrat", sans-serif;
  }
  .business-card {
    position: absolute;
    left: 58px;
    top: 183px;
    width: 1085px;
    height: 634px;
    background: var(--card-white);
    overflow: hidden;
  }
  .accent-circle {
    position: absolute;
    left: 0;
    top: 0;
    width: 1085px;
    height: 634px;
  }
  .brand-mark {
    position: absolute;
    left: 44px;
    top: 120px;
    display: flex;
    align-items: center;
    gap: 14px;
    color: var(--logo-orange);
    font-weight: 600;
    font-size: 34px;
    letter-spacing: 1px;
  }
  .brand-dot {
    width: 30px;
    height: 30px;
    border-radius: 50%;
    background: var(--logo-orange);
  }
  .contact-block {
    position: absolute;
    left: 547px;
    top: 308px;
    color: var(--text-light);
  }
  .person-name {
    font-size: 40px;
    font-weight: 600;
    line-height: 1.1;
  }
  .person-title {
    font-size: 26px;
    font-weight: 500;
    line-height: 1;
    margin-left: 2px;
  }
  .contact-list {
    list-style: none;
    margin-top: 70px;
    font-size: 26px;
    font-weight: 500;
  }
  .contact-list li { line-height: 39px; }
  .contact-list li:last-child { margin-top: 4px; }
</style>
</head>
<body>
  <div class="business-card">
    <svg class="accent-circle" viewBox="0 0 1085 634" role="img" aria-label="Orange circuit board photograph filling a large circular area">
      <defs>
        <radialGradient id="circuitTone" cx="0.75" cy="0.3" r="0.8">
          <stop offset="0" stop-color="var(--brand-orange-light)"/>
          <stop offset="1" stop-color="var(--brand-orange)"/>
        </radialGradient>
      </defs>
      <circle cx="892" cy="502" r="550" fill="url(#circuitTone)"/>
    </svg>

    <div class="brand-mark">
      <span class="brand-dot"></span>
      <span class="brand-name">TR Advisory</span>
    </div>

    <div class="contact-block">
      <h1 class="person-name">Dorian Fairweather</h1>
      <p class="person-title">Owner</p>
      <ul class="contact-list">
        <li>Office Phone - 555-714-3096</li>
        <li>Mobile Phone - 555-802-4173</li>
        <li>E-Mail - d@trvadvisory.example</li>
        <li>Website: www.trvadvisory.example</li>
      </ul>
    </div>
  </div>
</body>
</html>
```